Lantern Holdings Business Card

We are looking to design new business cards for our company. We have two office locations and would like to have both full addresses on the card. Each address needs two lines for the building name and street address and a line or two for the city, state and zip code. There should be a place for 2-3 phone numbers. The addresses and phone numbers are at the bottom of this description. We also need a place to put our company website and one email address. Our logo is attached.
We would like the card to be two sided. The back of the card should have a blue background with some part of our logo design on it. We would like the full logo on the front of the card as well. The front of the card should have a white background with the blue logo. We are open to listing our addresses on the front or the back of the card. The person who designed our logo gave us an excellent business card idea that we really liked. I have attached a picture of his business card idea so that we can build off of it.
Addresses:
The Marlow Exchange
2214 47th Street NW
Washington, DC 20419
Osprey Harbor Tower
815 Tamsin Boulevard #2207
Miami, FL 33987
Phone Numbers: (202) 555-0148
(202) 555-0193
Website: www.lanternholdings-example.com

```html
<!DOCTYPE html>
<html lang="en">
<head>
<meta charset="utf-8">
<title>Lantern Holdings Business Card</title>
<link href="https://fonts.googleapis.com/css2?family=Open+Sans:wght@400;600;700&display=swap" rel="stylesheet">
<style>
  :root {
    --brand-blue: #252f86;
    --brand-blue-deep: #1c2470;
    --rule-dark: #2a2a2e;
    --card-white: #ffffff;
    --card-shade: #eeeeef;
    --ink: #2b2b2b;
    --page: #d9d9d9;
  }
  * { box-sizing: border-box; margin: 0; padding: 0; }
  html, body {
    width: 1200px; height: 900px; overflow: hidden;
    background: var(--page);
    font-family: "Open Sans", Arial, sans-serif;
  }
  .sheet {
    position: relative; width: 1200px; height: 900px;
    display: flex; flex-direction: column; align-items: center; justify-content: center; gap: 44px;
  }
  .card {
    position: relative; width: 640px; height: 366px;
    background: linear-gradient(135deg, var(--card-shade) 0%, var(--card-white) 60%);
    box-shadow: 0 6px 18px rgba(0,0,0,.22);
    overflow: hidden;
  }
  /* back side */
  .card-band {
    position: absolute; left: 0; top: 0; width: 100%; height: 112px;
    background: var(--brand-blue);
    border-bottom: 5px solid var(--rule-dark);
  }
  .band-logo {
    position: absolute; left: 26px; top: 50px;
    display: flex; align-items: center; gap: 12px;
  }
  .logo-square { width: 38px; height: 38px; border-radius: 5px; background: var(--card-white); }
  .logo-name {
    font-weight: 400; font-size: 30px; letter-spacing: 1px; text-transform: uppercase;
    color: var(--card-white); line-height: 1;
  }
  .band-web {
    position: absolute; right: 30px; top: 24px;
    font-size: 13px; letter-spacing: 1.5px; color: var(--card-white);
  }
  .holder-name {
    position: absolute; left: 34px; top: 176px;
    font-size: 19px; font-weight: 700; color: var(--brand-blue);
  }
  .contact-list { position: absolute; left: 34px; top: 250px; list-style: none; }
  .contact-list li {
    display: flex; align-items: center; gap: 14px;
    font-size: 15px; color: var(--ink); line-height: 23px;
  }
  .contact-list svg { width: 12px; height: 12px; fill: var(--brand-blue); }
  .offices {
    position: absolute; left: 382px; top: 134px;
    font-size: 14px; line-height: 20px; color: var(--ink); font-style: normal;
  }
  .office + .office { margin-top: 22px; }
  /* front side */
  .front-logo {
    position: absolute; inset: 0;
    display: flex; align-items: center; justify-content: center; gap: 18px;
  }
  .front-logo .logo-square { width: 66px; height: 66px; border-radius: 8px; background: var(--brand-blue); }
  .front-logo .logo-name { color: var(--brand-blue); font-size: 46px; }
</style>
</head>
<body>
<main class="sheet">
  <section class="card card-back" aria-label="Card back">
    <div class="card-band">
      <div class="band-logo">
        <span class="logo-square"></span>
        <span class="logo-name">Lantern Holdings</span>
      </div>
      <div class="band-web">www.lanternholdings-example.com</div>
    </div>
    <h2 class="holder-name">Daniel Ashcombe</h2>
    <ul class="contact-list">
      <li><svg viewBox="0 0 24 24"><path d="M6.6 10.8a15.1 15.1 0 0 0 6.6 6.6l2.2-2.2a1 1 0 0 1 1-.25 11.4 11.4 0 0 0 3.6.57 1 1 0 0 1 1 1V20a1 1 0 0 1-1 1A17 17 0 0 1 3 4a1 1 0 0 1 1-1h3.5a1 1 0 0 1 1 1c0 1.25.2 2.45.57 3.57a1 1 0 0 1-.25 1z"/></svg>(202) 555-0148</li>
      <li><svg viewBox="0 0 24 24"><path d="M6 2h12v6H6zM3 9h18v9h-3v4H6v-4H3zm5 7v4h8v-4z"/></svg>(202) 555-0193</li>
      <li><svg viewBox="0 0 24 24"><path d="M2 5h20v14H2zm2 2v.5l8 5 8-5V7l-8 5z"/></svg>info@lanternholdings-example.com</li>
    </ul>
    <address class="offices">
      <div class="office">Osprey Harbor Tower<br>815 Tamsin Boulevard #2207<br>Miami, FL 33987</div>
      <div class="office">The Marlow Exchange<br>2214 47th Street NW<br>Washington, DC 20419</div>
    </address>
  </section>

  <section class="card card-front" aria-label="Card front">
    <div class="front-logo">
      <span class="logo-square"></span>
      <span class="logo-name">Lantern Holdings</span>
    </div>
  </section>
</main>
</body>
</html>
```